Milo's RV Park & Lodge Business Card

business card

Target Market(s)

RVers, Campers, Outdoor people, hunters, fishermen

Contact Information for Business Card

I would like a business card with a picture of my RV Park on one side and the following information on the other side:

Milo Hartvick
Milo's RV Park & Lodge
317 4th St NW
Leeds ND 58346
701-582-9017 (call)
701-624-7150 (call or text)
www.milosbrookfieldrvpark.example
milosbrookfield@mailbox.example

The color scheme is white with black and red

Colors
ec1f27
ffffff

Requirements
Must have
• picture of my rv park on one side

```html
<!DOCTYPE html>
<html lang="en">
<head>
<meta charset="utf-8">
<title>Milo's RV Park &amp; Lodge – Business Card</title>
<link rel="stylesheet" href="https://fonts.googleapis.com/css2?family=Lato:wght@400;700&display=swap">
<style>
  :root {
    --brand-red: #ec1f27;
    --ink: #1a1a1a;
    --paper: #ffffff;
    --stage: #e9e9eb;
    --sky-top: #8fa9d6;
    --sky-bottom: #d9e2ee;
    --tree: #3d5e2c;
    --gravel: #c9b79a;
    --grass: #4f8a2e;
  }
  * { box-sizing: border-box; margin: 0; padding: 0; }
  html, body { width: 1200px; height: 800px; overflow: hidden; }
  body {
    background: var(--stage);
    font-family: 'Lato', Arial, sans-serif;
    position: relative;
  }
  .card {
    position: absolute;
    width: 600px;
    height: 343px;
    background: var(--paper);
    border-bottom: 7px solid var(--brand-red);
    box-shadow: 0 10px 28px rgba(0,0,0,0.18);
    overflow: hidden;
  }
  .card--front { left: 110px; top: 36px; }
  .card--back  { left: 490px; top: 420px; }

  .park-photo {
    position: absolute;
    inset: 0;
    background: linear-gradient(180deg,
      var(--sky-top) 0%, var(--sky-bottom) 40%,
      var(--tree) 44%, var(--tree) 50%,
      var(--gravel) 52%, var(--gravel) 60%,
      var(--grass) 64%, var(--grass) 100%);
  }
  .front-title {
    position: absolute;
    top: 44px;
    width: 100%;
    text-align: center;
    color: var(--brand-red);
    font-weight: 700;
    font-size: 40px;
    letter-spacing: 0.5px;
    white-space: nowrap;
  }
  .front-url {
    position: absolute;
    right: 90px;
    bottom: 34px;
    color: var(--paper);
    font-weight: 700;
    font-size: 15px;
    letter-spacing: 0.3px;
  }

  .back-title {
    position: absolute;
    left: 48px;
    top: 58px;
    color: var(--brand-red);
    font-weight: 700;
    font-size: 40px;
    letter-spacing: 0.5px;
    white-space: nowrap;
  }
  .holder-name {
    position: absolute;
    right: 40px;
    top: 138px;
    color: var(--brand-red);
    font-weight: 700;
    font-size: 24px;
  }
  .divider {
    position: absolute;
    left: 60px;
    right: 36px;
    top: 174px;
    height: 1.5px;
    background: var(--ink);
  }
  .contact-list {
    position: absolute;
    left: 60px;
    top: 204px;
    list-style: none;
    color: var(--ink);
    font-size: 17px;
    line-height: 26px;
  }
  .contact-list li { display: flex; align-items: center; gap: 14px; }
  .contact-icon { width: 15px; height: 15px; fill: var(--brand-red); flex: none; }
  .address {
    position: absolute;
    right: 40px;
    top: 206px;
    text-align: right;
    color: var(--ink);
    font-size: 17px;
    line-height: 24px;
    font-style: normal;
  }
</style>
</head>
<body>

<section class="card card--front">
  <div class="park-photo" role="img" aria-label="Photo of the RV park: motorhomes and trailers parked along a gravel lot with trees behind and a green lawn in front"></div>
  <h1 class="front-title">MILO'S RV PARK &amp; LODGE</h1>
  <p class="front-url">www.milosbrookfieldrvpark.example</p>
</section>

<section class="card card--back">
  <h2 class="back-title">MILO'S RV PARK &amp; LODGE</h2>
  <p class="holder-name">Milo Hartvick</p>
  <div class="divider"></div>
  <ul class="contact-list">
    <li>
      <svg class="contact-icon" viewBox="0 0 24 24" aria-hidden="true"><path d="M6.6 10.8a15.1 15.1 0 0 0 6.6 6.6l2.2-2.2a1 1 0 0 1 1-.25 11.4 11.4 0 0 0 3.6.57 1 1 0 0 1 1 1V20a1 1 0 0 1-1 1A17 17 0 0 1 3 4a1 1 0 0 1 1-1h3.5a1 1 0 0 1 1 1c0 1.25.2 2.45.57 3.57a1 1 0 0 1-.25 1z"/></svg>
      701-582-9017 (call)
    </li>
    <li>
      <svg class="contact-icon" viewBox="0 0 24 24" aria-hidden="true"><path d="M6.6 10.8a15.1 15.1 0 0 0 6.6 6.6l2.2-2.2a1 1 0 0 1 1-.25 11.4 11.4 0 0 0 3.6.57 1 1 0 0 1 1 1V20a1 1 0 0 1-1 1A17 17 0 0 1 3 4a1 1 0 0 1 1-1h3.5a1 1 0 0 1 1 1c0 1.25.2 2.45.57 3.57a1 1 0 0 1-.25 1z"/></svg>
      701-624-7150 (call or text)
    </li>
    <li>
      <svg class="contact-icon" viewBox="0 0 24 24" aria-hidden="true"><path d="M2 5h20v14H2z M3.5 6.5 12 13l8.5-6.5" stroke="#fff" stroke-width="1.6"/></svg>
      milosbrookfield@mailbox.example
    </li>
    <li>
      <svg class="contact-icon" viewBox="0 0 24 24" aria-hidden="true"><circle cx="12" cy="12" r="10"/><path d="M2 12h20M12 2c3 3 3 17 0 20M12 2c-3 3-3 17 0 20" stroke="#fff" stroke-width="1.4" fill="none"/></svg>
      www.milosbrookfieldrvpark.example
    </li>
  </ul>
  <address class="address">317 4th St NW<br>Leeds, ND 58346</address>
</section>

</body>
</html>
```